Mirela Hastow ADHD coach needs a flyer

I need a flyer to be sent by email. the copy is attached. It can be changed/reduced to fit the flyer. I would like to keep my website colors. My website is www.mirelahastow.example - Thank you!

```html
<!DOCTYPE html>
<html lang="en">
<head>
<meta charset="utf-8">
<title>Mirela Hastow – Academic Success Coaching Flyer</title>
<link href="https://fonts.googleapis.com/css2?family=Josefin+Sans:ital,wght@0,300;0,400;0,600;1,300&display=swap" rel="stylesheet">
<style>
  :root {
    --slate: #6b7d84;
    --mist: #a0b6bf;
    --accent: #8aa3ad;
    --panel: #eef0f1;
    --ink: #3f4447;
    --paper: #ffffff;
    --page-bg: #eef0f2;
  }
  * { margin: 0; padding: 0; box-sizing: border-box; }
  html, body { width: 823px; height: 1200px; overflow: hidden; background: var(--page-bg); }
  body { font-family: "Josefin Sans", sans-serif; color: var(--ink); position: relative; }

  .flyer {
    position: absolute; left: 304px; top: 20px;
    width: 410px; height: 2210px;
    background: var(--paper);
    transform: scale(0.525); transform-origin: top left;
    box-shadow: 0 0 3px rgba(0,0,0,0.08);
  }
  .flyer > * { position: absolute; }

  .band { left: 0; width: 410px; background: var(--slate); color: #fff; text-align: center; }
  .band-top { top: 0; height: 147px; }
  .band-bottom { top: 2091px; height: 119px; }
  .band-title { font-weight: 600; font-size: 11.5px; letter-spacing: 2.2px; line-height: 19.5px; padding-top: 28px; }
  .band-rule { height: 1px; background: rgba(255,255,255,0.7); margin: 0 27px; }
  .band-top .band-rule { margin-top: 6px; }
  .band-sub { font-weight: 300; font-size: 7.6px; letter-spacing: 1.2px; line-height: 13.8px; padding-top: 7px; }
  .band-bottom .band-title { padding-top: 18px; padding-bottom: 14px; }
  .band-bottom .band-sub { padding-top: 16px; line-height: 10px; }

  .photo { background: linear-gradient(135deg, #8f9e9a, #a9b4b0 45%, #c8b8bd 75%, #7d8a88); }
  .portrait { left: 29px; top: 173px; width: 218px; height: 313px; z-index: 2; }
  .intro-box { left: 164px; top: 238px; width: 219px; height: 313px; background: var(--mist); color: #fff; }
  .intro-box svg { position: absolute; left: 130px; top: 22px; }
  .intro-text { position: absolute; font-weight: 300; font-size: 7.4px; letter-spacing: 1.1px; line-height: 13px; text-align: center; }
  .intro-text.upper { left: 88px; top: 70px; width: 127px; }
  .intro-text.lower { left: 8px; top: 258px; width: 203px; }

  .panel { background: var(--panel); }
  .about-panel { left: 27px; top: 578px; width: 242px; height: 260px; }
  .about-card { left: 46px; top: 597px; width: 233px; height: 223px; background: var(--paper); padding: 8px 14px;
    font-weight: 300; font-size: 7.4px; letter-spacing: 1px; line-height: 13.8px; text-align: center; }
  .side-line { left: 322px; top: 660px; width: 1px; height: 170px; background: var(--mist); }
  .side-note { left: 328px; top: 785px; width: 200px; transform: rotate(-90deg); transform-origin: top left;
    font-weight: 300; font-size: 6.8px; letter-spacing: 1px; line-height: 12px; color: var(--accent); }
  .group-panel { left: 73px; top: 797px; width: 310px; height: 218px; }
  .group-photo { left: 90px; top: 815px; width: 276px; height: 183px; background: linear-gradient(160deg, #b9b39e, #8f8a7a 50%, #6d7468); z-index: 2; }

  .section-head { left: 0; width: 410px; text-align: center; font-size: 11px; letter-spacing: 2px; line-height: 19px; }
  .section-head .lead { color: var(--accent); font-weight: 400; }
  .section-head .main { color: var(--slate); font-weight: 600; }
  .rule { height: 1px; background: #c4ced2; }

  .helps-aside { left: 40px; top: 1118px; width: 72px; text-align: right; font-weight: 300; font-size: 7.4px; letter-spacing: 1px; line-height: 13.8px; }
  .helps-line { left: 122px; top: 1120px; width: 1px; height: 260px; background: var(--ink); }
  .helps-box { left: 133px; top: 1120px; width: 250px; height: 260px; padding: 14px 12px; color: var(--mist); }
  .helps-box h3 { font-weight: 600; font-size: 7.4px; letter-spacing: 1px; line-height: 9px; text-align: center; color: var(--accent); margin-bottom: 12px; }
  .helps-box li { list-style: none; font-weight: 300; font-size: 6.8px; letter-spacing: 1px; line-height: 10px; margin-bottom: 10px; text-align: justify; }
  .helps-box li::before { content: "•"; margin-right: 4px; }

  .result-panel { left: 27px; top: 1490px; width: 356px; height: 171px; background: linear-gradient(90deg, #eaeaea, #d9d9d9 65%, #cfcfcf); }
  .student-figure { position: absolute; left: 235px; top: 18px; width: 110px; height: 153px; background: linear-gradient(180deg, #5a4b44, #c6c9cd 45%, #a2a6ab); border-radius: 40px 40px 0 0; }
  .result-text { position: absolute; left: 10px; top: 12px; width: 230px; font-size: 6.8px; letter-spacing: 0.8px; line-height: 12.5px; }
  .result-text li { list-style: none; }
  .result-text li::before { content: "• "; }
  .result-text strong { display: block; font-weight: 600; margin: 12px 0 10px; }

  .say-head { font-size: 11px; letter-spacing: 2px; color: var(--accent); font-weight: 400; }
  .quote { font-weight: 300; font-style: italic; font-size: 7.6px; letter-spacing: 1px; line-height: 12.5px; }
  .quote.right { text-align: right; }

  .footer-sub { font-size: 7.6px; }
</style>
</head>
<body>
<main class="flyer">
  <header class="band band-top">
    <h1 class="band-title">HELPING YOUR CHILD WITH ADHD<br>OR OTHER LEARNING CHALLENGES THRIVE<br>IN COLLEGE AND BEYOND</h1>
    <div class="band-rule"></div>
    <p class="band-sub">Academic success coaching that leads to lifelong transformation<br>for students with ADHD and similar challenges that may have<br>impeded their ability to thrive</p>
  </header>

  <div class="photo portrait" role="img" aria-label="Portrait photo of coach Mirela Hastow in a pale pink blazer"></div>
  <section class="intro-box">
    <svg width="46" height="32" viewBox="0 0 46 32" fill="none" stroke="#fff" stroke-width="1.2">
      <polyline points="1,1 23,23 45,1"/><polyline points="1,8 23,30 45,8"/>
    </svg>
    <p class="intro-text upper">Sending your child off to college can feel scary, especially if that college is hundreds of miles away. You worry about how they'll do on their own—whether they'll make friends, earn good grades, and be happy—especially without you there to support them daily. You know your child is bright, and you want</p>
    <p class="intro-text lower">them to have a great future, but you're concerned they will struggle without the right support and resources.</p>
  </section>

  <div class="panel about-panel"></div>
  <p class="about-card">You don't need to feel helpless as you send your child off to this next stage of their lives. Mirela is dedicated to making that transition easier for everyone. Mirela Hastow has years of experience helping students thrive despite their challenges. She sees your child's potential and helps them see it, too. She provides a safety net as they adjust to a new environment at college. Her services are comprehensive and adaptable, based on the requirements of each individual: helping with course selection and scheduling, time management, study strategies, focus, making new friends, and adapting to change.</p>
  <div class="side-line"></div>
  <p class="side-note">Mirela guides students through fundamental work on mindset to ensure that changes stick.</p>
  <div class="panel group-panel"></div>
  <div class="group-photo" role="img" aria-label="Photo of a smiling group of college students outdoors holding books"></div>

  <h2 class="section-head" style="top:1047px"><span class="lead">EMPOWERING FOCUS:</span><br><span class="main">HOW MIRELA HELPS</span></h2>
  <div class="rule" style="left:27px;top:1098px;width:356px"></div>

  <p class="helps-aside">Mirela has taken students from failing to a 3.0 GPA, and from a C student to the Dean's List, in just one semester. It doesn't take years to provide lasting results; all it takes is the right guide.</p>
  <div class="helps-line"></div>
  <section class="panel helps-box">
    <h3>UNIQUELY POSITIONED<br>TO HELP YOUR CHILD, MIRELA:</h3>
    <ul>
      <li>Tailors support so that your child improves focus and maximizes their potential in college and beyond.</li>
      <li>Understands your child's unique needs - she sees the gifts that others often miss.</li>
      <li>Knows the academic landscape intimately, including the challenges faced by students with ADHD and other conditions.</li>
      <li>Helps with the logistics of scheduling in a way that most advisors can't, enrolling students in the courses that best suit their learning style.</li>
      <li>Nurtures the brilliance in your bright child.</li>
      <li>Provides a balance between encouraging students and challenging them.</li>
    </ul>
  </section>

  <h2 class="section-head" style="top:1418px"><span class="lead">REALIZING POTENTIAL:</span><br><span class="main">THE TRANSFORMATION YOU'LL SEE IN YOU CHILD</span></h2>
  <div class="rule" style="left:27px;top:1469px;width:356px"></div>

  <section class="result-panel">
    <div class="student-figure" role="img" aria-label="Photo of a cheerful student holding notebooks"></div>
    <div class="result-text">
      <ul>
        <li>A mindset of self-belief and increased confidence.</li>
        <li>Higher grades and the drive to graduate.</li>
        <li>Social integration and making friends.</li>
        <li>Happiness and fulfilment.</li>
        <li>A deep sense of personal achievement and pride.</li>
      </ul>
      <strong>You Will Have:</strong>
      <ul>
        <li>Fewer sleepless nights worrying about your child.</li>
        <li>Less stress, knowing that your child is in good hands.</li>
        <li>Confidence that they are receiving the right support.</li>
        <li>Joy and pride at seeing them do well.</li>
      </ul>
    </div>
  </section>

  <h2 class="say-head" style="left:27px;top:1698px">WHAT PARENTS SAY</h2>
  <div class="rule" style="left:27px;top:1730px;width:210px"></div>
  <p class="quote" style="left:36px;top:1750px;width:280px">"Mirela was the glue that kept our daughter in college... as our daughter's Academic Coach, [she] gave our daughter the ability to finish strong by empowering her with the skills needed to be successful." — Lorna</p>
  <p class="quote" style="left:32px;top:1820px;width:290px">"Mirela has always told my daughter not that she can succeed, but that she will succeed." — Beth</p>

  <h2 class="say-head" style="left:172px;top:1879px;width:211px;text-align:right">WHAT STUDENT SAY</h2>
  <div class="rule" style="left:172px;top:1912px;width:211px"></div>
  <p class="quote right" style="left:110px;top:1932px;width:273px">"Last semester I completed all 16 hours and I had the highest GPA I've ever had!" — Former student</p>
  <p class="quote right" style="left:118px;top:1973px;width:265px;text-align:justify">"Under her instruction, my grades began to improve. I ended up making the Dean's List during my time at Westbrook, and I was also inducted into Theta Rho Sigma. I am currently in my first year of law school at Ashford Crest University, a top tier school." — Former student</p>

  <footer class="band band-bottom">
    <h2 class="band-title">NEXT STEP</h2>
    <div class="band-rule"></div>
    <p class="band-sub footer-sub">To learn more and discuss your child's individual needs,<br>call 555.014.2290<br>or email coach@mirelahastow.example</p>
  </footer>
</main>
</body>
</html>
```